WBP Business Cards

I need business cards for "willow bend partners llc" doublesided... logo on the back (also include logo on front)
logo attached to project... i have jpg up.. let me know if you need eps file.
Company Info:
742 East Harlow Avenue, Suite 8D
Chicago, Illinois 60417
facsimile 312-481-2267 (list fax, address, website on all cards.)
www.willowbendpartnersllc.example
Three different people on cards:
Darius K. Whitcomb, CPA MST
Principal
ofc 312-481-3900
mobile 312-574-8816
dariuskwhitcomb@willowbendpartnersllc.example
Peter J. Olundsen, CPA MST
Principal
peterjolundsen@willowbendpartnersllc.example
mobile 708-613-4471
ofc 312-481-3900
Alvin M Crandby
Principal
ofc 312-481-3900
no mobile
alvinmcrandby@willowbendpartnersllc.example
I have multiple projects listed.. see below:
Business cards for willow bend partners llc
letterhead
envelopes
Business cards for KT Holdings LLC
letterhead
envelopes
Target Market(s)
rich people
Industry/Entity Type
Business
Look and feel

```html
<!DOCTYPE html>
<html lang="en">
<head>
<meta charset="utf-8">
<title>WBP Business Cards</title>
<link href="https://fonts.googleapis.com/css2?family=Arimo:wght@400&family=Archivo+Narrow:wght@400&display=swap" rel="stylesheet">
<style>
  :root {
    --navy: #173f72;
    --stage: #2a2a2a;
    --stage-light: #4a4a4a;
    --back-grey: #c6c6c6;
    --white: #ffffff;
    --ink: #173f72;
  }
  * { margin: 0; padding: 0; box-sizing: border-box; }
  html, body { width: 1200px; height: 1000px; overflow: hidden; }
  body {
    position: relative;
    background: radial-gradient(ellipse at 50% 40%, var(--stage-light), var(--stage) 75%);
    font-family: "Archivo Narrow", "Arial Narrow", sans-serif;
  }
  .card {
    position: absolute;
    width: 500px;
    height: 292px;
    overflow: hidden;
  }
  .card--back { left: 73px; background: var(--back-grey); }
  .card--front { left: 625px; background: var(--white); }
  .row-1 { top: 23px; }
  .row-2 { top: 348px; }
  .row-3 { top: 669px; }

  /* back side brand */
  .brand-back {
    position: absolute;
    inset: 0;
    display: flex;
    flex-direction: column;
    align-items: center;
    justify-content: center;
    gap: 22px;
  }
  .brand-back .brand-dot {
    width: 90px; height: 90px; border-radius: 50%; background: var(--navy);
  }
  .brand-back .brand-name {
    font-family: "Arimo", Arial, sans-serif;
    font-size: 24px;
    letter-spacing: 1.5px;
    color: var(--navy);
    text-transform: uppercase;
  }

  /* front side brand */
  .brand-front {
    position: absolute;
    top: 28px;
    right: 32px;
    display: flex;
    flex-direction: column;
    align-items: center;
  }
  .brand-front .brand-dot {
    width: 46px; height: 46px; border-radius: 50%; background: var(--navy); margin-bottom: 10px;
  }
  .brand-front .brand-name {
    font-family: "Arimo", Arial, sans-serif;
    font-size: 13px;
    letter-spacing: 0.8px;
    color: var(--navy);
    text-transform: uppercase;
  }
  .brand-front .brand-url {
    font-family: "Arimo", Arial, sans-serif;
    font-size: 10px;
    letter-spacing: 1px;
    color: var(--navy);
    margin-top: 2px;
  }

  .name-band {
    position: absolute;
    left: 0;
    top: 145px;
    width: 304px;
    height: 40px;
    background: var(--navy);
    color: var(--white);
    padding: 3px 0 0 24px;
  }
  .row-3 .name-band { top: 143px; }
  .person-name { font-size: 20px; line-height: 21px; }
  .person-title { font-size: 12px; line-height: 13px; }

  .contact {
    position: absolute;
    left: 24px;
    top: 192px;
    color: var(--ink);
    font-size: 11.5px;
    line-height: 15.3px;
  }
  .row-3 .contact { top: 203px; }
  .contact .gap { margin-top: 5px; }

  .foot-band {
    position: absolute;
    left: 0; right: 0; bottom: 0;
    height: 12px;
    background: var(--navy);
  }
</style>
</head>
<body>

  <!-- Row 1 -->
  <section class="card card--back row-1">
    <div class="brand-back">
      <span class="brand-dot"></span>
      <span class="brand-name">Willow Bend Partners LLC</span>
    </div>
  </section>
  <section class="card card--front row-1">
    <div class="brand-front">
      <span class="brand-dot"></span>
      <span class="brand-name">Willow Bend Partners LLC</span>
      <span class="brand-url">www.willowbendpartnersllc.example</span>
    </div>
    <div class="name-band">
      <p class="person-name">Darius K. Whitcomb, CPA MST</p>
      <p class="person-title">Principal</p>
    </div>
    <div class="contact">
      <p>Office : 312-481-3900</p>
      <p>Mobile : 312-574-8816</p>
      <p>Email : dariuskwhitcomb@willowbendpartnersllc.example</p>
      <p class="gap">Facsimile : 312-481-2267</p>
      <p>Address : 742 East Harlow Avenue, Suite 8D Chicago, Illinois 60417.</p>
    </div>
    <div class="foot-band"></div>
  </section>

  <!-- Row 2 -->
  <section class="card card--back row-2">
    <div class="brand-back">
      <span class="brand-dot"></span>
      <span class="brand-name">Willow Bend Partners LLC</span>
    </div>
  </section>
  <section class="card card--front row-2">
    <div class="brand-front">
      <span class="brand-dot"></span>
      <span class="brand-name">Willow Bend Partners LLC</span>
      <span class="brand-url">www.willowbendpartnersllc.example</span>
    </div>
    <div class="name-band">
      <p class="person-name">Peter J. Olundsen, CPA MST</p>
      <p class="person-title">Principal</p>
    </div>
    <div class="contact">
      <p>Office : 312-481-3900</p>
      <p>Mobile : 708-613-4471</p>
      <p>Email : peterjolundsen@willowbendpartnersllc.example</p>
      <p class="gap">Facsimile : 312-481-2267</p>
      <p>Address : 742 East Harlow Avenue, Suite 8D Chicago, Illinois 60417.</p>
    </div>
    <div class="foot-band"></div>
  </section>

  <!-- Row 3 -->
  <section class="card card--back row-3">
    <div class="brand-back">
      <span class="brand-dot"></span>
      <span class="brand-name">Willow Bend Partners LLC</span>
    </div>
  </section>
  <section class="card card--front row-3">
    <div class="brand-front">
      <span class="brand-dot"></span>
      <span class="brand-name">Willow Bend Partners LLC</span>
      <span class="brand-url">www.willowbendpartnersllc.example</span>
    </div>
    <div class="name-band">
      <p class="person-name">Alvin M Crandby</p>
      <p class="person-title">Principal</p>
    </div>
    <div class="contact">
      <p>Office : 312-481-3900</p>
      <p>Email : alvinmcrandby@willowbendpartnersllc.example</p>
      <p class="gap">Facsimile : 312-481-2267</p>
      <p>Address : 742 East Harlow Avenue, Suite 8D Chicago, Illinois 60417.</p>
    </div>
    <div class="foot-band"></div>
  </section>

</body>
</html>
```